Business Card for a Wedding Films Business

We require a business card design for our business 'Lewis Marrow Wedding Films'. The logo needs to look classy and high end.

Target Market(s)

Wedding Couples

Contact Information for Business Card

Lewis Marrow Wedding Films
07312 605 227
films@lewismarrowreels.com
www.lewismarrowreels.com

Facebook: @lewismarrowweddingfilms
Instagram: @lewismarrowfilms

Font styles to use
Sans Serif

Requirements
Must have
• Social media icons - Facebook and Instagram

```html
<!DOCTYPE html>
<html lang="en">
<head>
<meta charset="utf-8">
<title>Lewis Marrow Wedding Films — Business Card</title>
<link rel="stylesheet" href="https://fonts.googleapis.com/css2?family=Jost:wght@400;500;600&display=swap">
<style>
  :root {
    --page: #d6d6d8;
    --card-light: #e9e8f2;
    --card-dark: #2e2e30;
    --ink: #1f1f21;
    --ink-soft: #4a4a4e;
    --rule: #9a9aa0;
    --on-dark: #ffffff;
  }
  * { box-sizing: border-box; margin: 0; padding: 0; }
  html, body {
    width: 1200px; height: 892px; overflow: hidden;
    background: var(--page);
    font-family: "Jost", sans-serif;
  }
  .canvas { position: relative; width: 1200px; height: 892px; }

  .card {
    position: absolute;
    width: 620px; height: 354px;
    border-radius: 22px;
    overflow: hidden;
  }

  /* Front */
  .card-front { left: 70px; top: 90px; background: var(--card-light); color: var(--ink); }
  .brand-block {
    position: absolute; left: 0; top: 0; width: 300px; height: 266px;
    display: flex; flex-direction: column; align-items: center; justify-content: center;
  }
  .brand-name {
    font-weight: 500; font-size: 27px; letter-spacing: 5px; line-height: 1;
  }
  .brand-tag {
    font-weight: 500; font-size: 11px; letter-spacing: 7px; margin-top: 8px;
  }
  .divider {
    position: absolute; left: 300px; top: 70px; width: 1px; height: 130px;
    background: var(--rule);
  }
  .contact-block {
    position: absolute; left: 336px; top: 72px;
  }
  .contact-title {
    font-weight: 600; font-size: 23px; line-height: 1.05; letter-spacing: 0.2px;
    text-transform: uppercase; margin-bottom: 14px;
  }
  .contact-list { list-style: none; }
  .contact-list li {
    display: flex; align-items: center; gap: 8px;
    font-size: 15px; color: var(--ink-soft); line-height: 1.45;
  }
  .contact-list svg { width: 13px; height: 13px; flex: none; }

  .social-band {
    position: absolute; left: 0; right: 0; top: 266px; height: 44px;
    background: var(--card-dark);
    display: flex; align-items: center; justify-content: space-around;
    padding: 0 30px;
  }
  .social-item {
    display: flex; align-items: center; gap: 8px;
    color: var(--on-dark); font-size: 15px;
  }
  .social-dot { width: 13px; height: 13px; border-radius: 50%; background: var(--on-dark); }

  /* Back */
  .card-back {
    left: 510px; top: 470px; background: var(--card-dark);
    display: flex; align-items: center; justify-content: center;
    box-shadow: 0 2px 0 #1a1a1b;
  }
  .back-name {
    color: var(--on-dark); font-weight: 500; font-size: 30px; letter-spacing: 7px;
  }
</style>
</head>
<body>
<main class="canvas">
  <section class="card card-front" aria-label="Business card front">
    <div class="brand-block">
      <div class="brand-name">LEWIS MARROW</div>
      <div class="brand-tag">WEDDING FILMS</div>
    </div>
    <div class="divider"></div>
    <div class="contact-block">
      <h1 class="contact-title">Lewis Marrow<br>Wedding Films</h1>
      <ul class="contact-list">
        <li>
          <svg viewBox="0 0 16 16"><path fill="#2e2e30" d="M4 1.5l2.2 3-1.3 1.6a9 9 0 0 0 5 5l1.6-1.3 3 2.2-1.4 2.5C7.5 14.5 1.5 8.5 1.5 2.9z"/></svg>
          07312 605 227
        </li>
        <li>
          <svg viewBox="0 0 16 16"><rect x="1" y="3" width="14" height="10" fill="#2e2e30"/><path d="M1.5 3.5L8 9l6.5-5.5" fill="none" stroke="#e9e8f2" stroke-width="1.2"/></svg>
          films@lewismarrowreels.com
        </li>
        <li>
          <svg viewBox="0 0 16 16"><circle cx="8" cy="8" r="7" fill="#2e2e30"/><path d="M1 8h14M8 1c-3 3.5-3 10.5 0 14M8 1c3 3.5 3 10.5 0 14" fill="none" stroke="#e9e8f2" stroke-width="0.9"/></svg>
          www.lewismarrowreels.com
        </li>
      </ul>
    </div>
    <div class="social-band">
      <span class="social-item"><span class="social-dot"></span>@lewismarrowweddingfilms</span>
      <span class="social-item"><span class="social-dot"></span>@lewismarrowfilms</span>
    </div>
  </section>

  <section class="card card-back" aria-label="Business card back">
    <div class="back-name">LEWIS MARROW</div>
  </section>
</main>
</body>
</html>
```